Accounting Business needs double sided DL flyer design

We need a double sided DL flyer designed,
Front side with logo, web address and our short intro.
Backside to have a list of services.
Our colours are blue and a concrete grey colour. Look at our website for a feel for our colour scheme.
www.lanternwellgroup.com.au
I have included the pic from our website to possibly use but we are also open to new creative ideas.
Target Market(s)
Our target market are proactive business owners, particularly in the wine and hospitality industry.
Industry/Entity Type
Business
Look and feel

```html
<!DOCTYPE html>
<html lang="en">
<head>
<meta charset="utf-8">
<title>Lanternwell Group – DL Flyer</title>
<link rel="stylesheet" href="https://fonts.googleapis.com/css2?family=Montserrat:wght@400;500;600&display=swap">
<style>
  :root {
    --page-bg: #e9e6e1;
    --sky-top: #2f6c86;
    --sky-mid: #7fa6b6;
    --haze: #d9d2c3;
    --glow: #e39a4a;
    --cloud-dark: #1d3444;
    --night: #0f1d2a;
    --ink-light: #f4f4f2;
    --ink-soft: #d7dde1;
    --concrete: #9aa2a6;
  }
  * { box-sizing: border-box; margin: 0; padding: 0; }
  html, body { width: 1200px; height: 844px; overflow: hidden; }
  body {
    background: var(--page-bg);
    font-family: "Montserrat", sans-serif;
    display: flex;
    align-items: center;
    justify-content: center;
    gap: 50px;
  }
  .flyer {
    position: relative;
    width: 362px;
    height: 764px;
    overflow: hidden;
    color: var(--ink-light);
    box-shadow: 0 10px 28px rgba(0,0,0,0.22);
  }
  .flyer__photo {
    position: absolute;
    inset: 0;
    background:
      radial-gradient(ellipse 80% 18% at 55% 52%, rgba(246,178,96,0.95), rgba(227,154,74,0) 70%),
      linear-gradient(180deg,
        var(--sky-top) 0%,
        var(--sky-mid) 22%,
        var(--haze) 40%,
        var(--glow) 52%,
        #a0653a 58%,
        var(--cloud-dark) 68%,
        var(--night) 100%);
  }
  .intro {
    position: absolute;
    left: 36px;
    right: 36px;
    bottom: 150px;
    font-size: 12px;
    line-height: 1.6;
    letter-spacing: 0.3px;
    color: var(--ink-soft);
  }
  .brand {
    position: absolute;
    left: 36px;
    right: 30px;
    bottom: 70px;
    display: flex;
    align-items: center;
    gap: 14px;
  }
  .brand__mark {
    width: 32px;
    height: 32px;
    border: 3px solid var(--ink-soft);
    flex: none;
  }
  .brand__text { flex: 1; }
  .brand__name {
    font-weight: 600;
    font-size: 17px;
    letter-spacing: 1.5px;
    text-transform: uppercase;
    color: var(--ink-soft);
    line-height: 1.1;
    white-space: nowrap;
  }
  .brand__tagline {
    margin-top: 6px;
    padding-top: 5px;
    border-top: 1px solid var(--concrete);
    font-size: 7px;
    letter-spacing: 1.8px;
    text-transform: uppercase;
    color: var(--ink-soft);
    font-weight: 400;
    white-space: nowrap;
  }
  .web {
    position: absolute;
    left: 36px;
    right: 30px;
    bottom: 32px;
    font-size: 11px;
    letter-spacing: 1px;
    color: var(--ink-soft);
  }
  .services {
    position: absolute;
    top: 40px;
    left: 34px;
    right: 20px;
  }
  .services__title {
    display: inline-block;
    font-weight: 400;
    font-size: 27px;
    letter-spacing: 1px;
    padding: 8px 0 5px 22px;
    border-top: 2px solid var(--ink-light);
    border-bottom: 2px solid var(--ink-light);
    margin-bottom: 12px;
  }
  .services__list {
    list-style: none;
    font-size: 12px;
    line-height: 1.55;
    letter-spacing: 0.4px;
  }
  .services__list li::before {
    content: "";
    display: inline-block;
    width: 4px;
    height: 4px;
    border-radius: 50%;
    background: var(--ink-light);
    margin: 0 9px 2px 0;
    vertical-align: middle;
  }
</style>
</head>
<body>

  <section class="flyer flyer--front">
    <div class="flyer__photo" role="img" aria-label="Paraglider silhouetted against a sunset sky above a sea of clouds"></div>
    <p class="intro">Proactive advice for business owners who want clearer numbers, stronger growth and more time for what matters.</p>
    <div class="brand">
      <span class="brand__mark"></span>
      <div class="brand__text">
        <div class="brand__name">Lanternwell Group</div>
        <div class="brand__tagline">Business Advisors &amp; Accountants</div>
      </div>
    </div>
    <p class="web">www.lanternwellgroup.com.au</p>
  </section>

  <section class="flyer flyer--back">
    <div class="flyer__photo" role="img" aria-label="Sunset sky glowing above a layer of clouds"></div>
    <div class="services">
      <h2 class="services__title">Our Services</h2>
      <ul class="services__list">
        <li>Taxation Compliance</li>
        <li>Financial &amp; Management Reporting</li>
        <li>Self-Managed Superannuation</li>
        <li>Virtual CFO</li>
        <li>Business Planning</li>
        <li>KPIs &amp; Performance Monitoring</li>
        <li>Succession Planning</li>
        <li>Estate Planning</li>
        <li>Cloud Solutions</li>
        <li>Business Support Services</li>
        <li>The Wine Industry</li>
      </ul>
    </div>
    <div class="brand">
      <span class="brand__mark"></span>
      <div class="brand__text">
        <div class="brand__name">Lanternwell Group</div>
        <div class="brand__tagline">Business Advisors &amp; Accountants</div>
      </div>
    </div>
  </section>

</body>
</html>
```